Design for online reviews widget

Attached is a wireframe of a widget we need designing to display reviews on websites from multiple sources. We need this provided at 3 different sizes including full screen, contained (like the wireframe) and mobile.
You have completely free rein on the styling.
The only elements that should remain untouched are the blue stars (https://www.filevault-demo.net/s/8pwtmz2lq4nv90h/kt%20stars.ai?dl=0) and powered by logo at the bottom.
Ignore the menu at the top of the wireframe, this is just from the website the widget will be placed on.
Target Market(s)
Businesses
Look and feel
Each slider illustrates characteristics of the customer's brand and the style your logo design should communicate.

```html
<!DOCTYPE html>
<html lang="en">
<head>
<meta charset="utf-8">
<title>Reviews Widget</title>
<link href="https://fonts.googleapis.com/css2?family=Inter:wght@400;500;600;700;800&display=swap" rel="stylesheet">
<style>
:root{
  --blue:#38bdf0;
  --blue-pale:#c9ecfb;
  --ink:#0d0f14;
  --muted:#9aa0a8;
  --body:#6f7680;
  --card:#fafcfe;
  --badge:#f1f7fd;
  --lavender:#e6e6fb;
  --white:#ffffff;
}
*{box-sizing:border-box;margin:0;padding:0}
html,body{width:1200px;height:1061px;overflow:hidden;background:var(--white);font-family:"Inter",sans-serif;color:var(--ink)}
.canvas{position:relative;width:1200px;height:1061px}
.star{display:block}
.hero-stars{position:absolute;left:26px;top:0;display:flex;gap:13px}
.hero-stars .star{width:66px;height:66px}

.panel{position:absolute;background:linear-gradient(120deg,#ffffff 10%,var(--lavender) 45%,#f6f6fd 70%,#ffffff 100%);box-shadow:0 10px 30px rgba(40,50,90,.10)}
.panel-desktop{left:26px;top:118px;width:847px;height:910px;border-radius:26px}
.panel-mobile{left:940px;top:118px;width:252px;height:554px;border-radius:16px;overflow:hidden}

.head-stars{position:absolute;display:flex}
.panel-desktop .head-stars{left:55px;top:51px;gap:4px}
.panel-desktop .head-stars .star{width:24px;height:24px}
.title{position:absolute;font-weight:800;letter-spacing:-.5px}
.panel-desktop .title{left:55px;top:78px;font-size:36px}
.subtitle{position:absolute;color:var(--muted)}
.panel-desktop .subtitle{left:55px;top:118px;font-size:13px}

.filter{position:absolute;left:618px;top:44px;width:172px;height:34px;border-radius:17px;background:#e9eef2;display:flex;align-items:center;justify-content:space-between;padding:0 20px 0 22px;font-size:11px;color:#6a7078}
.filter svg{width:12px;height:8px}

.review{position:absolute;background:var(--card);box-shadow:0 4px 14px rgba(40,50,90,.07)}
.panel-desktop .review{left:55px;width:731px;height:140px;border-radius:16px}
.review h3{font-weight:600}
.panel-desktop .review h3{position:absolute;left:28px;top:24px;font-size:16px}
.panel-desktop .review p{position:absolute;left:28px;top:52px;width:480px;font-size:10.5px;line-height:13px;color:var(--body)}
.scores{position:absolute;color:var(--ink)}
.panel-desktop .scores{left:28px;top:85px;font-size:10.5px}
.scores b{font-weight:600}
.meta{position:absolute;color:var(--blue)}
.panel-desktop .meta{left:30px;top:105px;font-size:10.5px}

.review.active{background:var(--blue);box-shadow:0 8px 16px rgba(40,120,170,.28)}
.review.active h3,.review.active .meta{color:var(--white)}
.review.active p{color:#bfe9fa}
.review.active .scores{color:#1e3b4c}

.badge{position:absolute;background:var(--badge);box-shadow:0 4px 8px rgba(40,50,90,.08);display:flex;flex-direction:column;align-items:center;justify-content:center}
.panel-desktop .badge{left:555px;top:12px;width:160px;height:116px;border-radius:24px;gap:8px}
.review.active .badge{background:var(--white)}
.brand{font-weight:600;color:#1d2330}
.panel-desktop .brand{font-size:15px}
.badge-stars{display:flex}
.panel-desktop .badge-stars{gap:2px}
.panel-desktop .badge-stars .star{width:19px;height:19px}
.rating{font-weight:500}
.panel-desktop .rating{font-size:14px}

.load{position:absolute;background:var(--blue);color:var(--white);display:flex;align-items:center;justify-content:center;font-weight:600;letter-spacing:.5px}
.panel-desktop .load{left:312px;top:835px;width:220px;height:37px;border-radius:19px;font-size:11px}

/* mobile */
.panel-mobile .head-stars{left:14px;top:32px;gap:3px}
.panel-mobile .head-stars .star{width:17px;height:17px}
.panel-mobile .title{left:14px;top:56px;font-size:21px;letter-spacing:0}
.panel-mobile .subtitle{left:14px;top:82px;font-size:8px}
.filter-round{position:absolute;left:208px;top:55px;width:30px;height:30px;border-radius:50%;background:var(--blue);display:flex;align-items:center;justify-content:center}
.panel-mobile .review{left:12px;width:226px;height:75px;border-radius:10px}
.panel-mobile .review h3{position:absolute;left:13px;top:14px;width:130px;font-size:8.5px;line-height:9px}
.panel-mobile .review p{position:absolute;left:13px;top:36px;width:125px;font-size:3.2px;line-height:4.5px;color:var(--body)}
.panel-mobile .scores{left:13px;top:49px;font-size:4px}
.panel-mobile .meta{left:13px;top:57px;font-size:4px}
.panel-mobile .badge{left:150px;top:11px;width:67px;height:52px;border-radius:9px;gap:3px}
.panel-mobile .brand{font-size:6.5px}
.panel-mobile .badge-stars{gap:1px}
.panel-mobile .badge-stars .star{width:8.5px;height:8.5px}
.panel-mobile .rating{font-size:6px}
.panel-mobile .load{left:10px;top:460px;width:226px;height:24px;border-radius:12px;font-size:7.5px}
.nav{position:absolute;left:0;top:499px;width:252px;height:55px;background:var(--white);display:flex;justify-content:space-around;padding:14px 14px 0}
.nav-item{display:flex;flex-direction:column;align-items:center;gap:3px;font-size:6.5px;color:#8a9098;width:36px}
.nav-item svg{width:12px;height:12px;fill:none;stroke:#6a7078;stroke-width:1.3}
.nav-item.current{color:var(--ink)}
.nav-item.current svg{stroke:var(--ink)}
</style>
</head>
<body>
<svg width="0" height="0" style="position:absolute">
  <defs>
    <symbol id="star" viewBox="-1 -1 2 2">
      <circle r="1" fill="#38bdf0"/>
      <path d="M0,-0.62 L0.153,-0.21 0.59,-0.19 0.247,0.08 0.364,0.5 0,0.26 -0.364,0.5 -0.247,0.08 -0.59,-0.19 -0.153,-0.21Z" fill="#fff" stroke="#fff" stroke-width="0.08" stroke-linejoin="round" transform="rotate(12)"/>
    </symbol>
    <symbol id="star-pale" viewBox="-1 -1 2 2">
      <circle r="1" fill="#c9ecfb"/>
      <path d="M0,-0.62 L0.153,-0.21 0.59,-0.19 0.247,0.08 0.364,0.5 0,0.26 -0.364,0.5 -0.247,0.08 -0.59,-0.19 -0.153,-0.21Z" fill="#fff" stroke="#fff" stroke-width="0.08" stroke-linejoin="round" transform="rotate(12)"/>
    </symbol>
  </defs>
</svg>

<div class="canvas">
  <div class="hero-stars">
    <svg class="star"><use href="#star"/></svg><svg class="star"><use href="#star"/></svg><svg class="star"><use href="#star"/></svg><svg class="star"><use href="#star"/></svg><svg class="star"><use href="#star"/></svg>
  </div>

  <section class="panel panel-desktop">
    <div class="head-stars">
      <svg class="star"><use href="#star"/></svg><svg class="star"><use href="#star"/></svg><svg class="star"><use href="#star"/></svg><svg class="star"><use href="#star"/></svg><svg class="star"><use href="#star"/></svg>
    </div>
    <h1 class="title">Reviews</h1>
    <div class="subtitle">Combined Review Score 4.3 out of 5</div>
    <div class="filter">Filter Results<svg viewBox="0 0 12 8"><path d="M1 1.5l5 5 5-5" fill="none" stroke="#38bdf0" stroke-width="2" stroke-linecap="round" stroke-linejoin="round"/></svg></div>

    <article class="review" style="top:162px">
      <h3>Front door with windows each side and side window</h3>
      <p>Lorem ipsum dolor sit amet, consectetur adipiscing elit. Tristique elementum maecenas purus dignissim felis. Phasellus tortor rhoncus a venenatis non sem. Id viverra vulputate eleifend.</p>
      <div class="scores"><b>Reliability</b>: 9.38 <b>Courtesy</b>:10 <b>Tidiness</b>:9.84</div>
      <div class="meta">Verified 28th September 2021 | Located in Brentwood</div>
      <div class="badge"><div class="brand">Fixrated.net</div><div class="badge-stars"><svg class="star"><use href="#star"/></svg><svg class="star"><use href="#star"/></svg><svg class="star"><use href="#star"/></svg><svg class="star"><use href="#star"/></svg><svg class="star"><use href="#star-pale"/></svg></div><div class="rating">4.2</div></div>
    </article>

    <article class="review active" style="top:328px">
      <h3>Front door with windows each side and side window</h3>
      <p>Lorem ipsum dolor sit amet, consectetur adipiscing elit. Tristique elementum maecenas purus dignissim felis. Phasellus tortor rhoncus a venenatis non sem. Id viverra vulputate eleifend.</p>
      <div class="scores"><b>Reliability</b>: 9.38 <b>Courtesy</b>:10 <b>Tidiness</b>:9.84</div>
      <div class="meta">Verified 28th September 2021 | Located in Brentwood</div>
      <div class="badge"><div class="brand">Fixrated.net</div><div class="badge-stars"><svg class="star"><use href="#star"/></svg><svg class="star"><use href="#star"/></svg><svg class="star"><use href="#star"/></svg><svg class="star"><use href="#star"/></svg><svg class="star"><use href="#star-pale"/></svg></div><div class="rating">4.2</div></div>
    </article>

    <article class="review" style="top:493px">
      <h3>Front door with windows each side and side window</h3>
      <p>Lorem ipsum dolor sit amet, consectetur adipiscing elit. Tristique elementum maecenas purus dignissim felis. Phasellus tortor rhoncus a venenatis non sem. Id viverra vulputate eleifend.</p>
      <div class="scores"><b>Reliability</b>: 9.38 <b>Courtesy</b>:10 <b>Tidiness</b>:9.84</div>
      <div class="meta">Verified 28th September 2021 | Located in Brentwood</div>
      <div class="badge"><div class="brand">Fixrated.net</div><div class="badge-stars"><svg class="star"><use href="#star"/></svg><svg class="star"><use href="#star"/></svg><svg class="star"><use href="#star"/></svg><svg class="star"><use href="#star"/></svg><svg class="star"><use href="#star-pale"/></svg></div><div class="rating">4.2</div></div>
    </article>

    <article class="review" style="top:659px">
      <h3>Front door with windows each side and side window</h3>
      <p>Lorem ipsum dolor sit amet, consectetur adipiscing elit. Tristique elementum maecenas purus dignissim felis. Phasellus tortor rhoncus a venenatis non sem. Id viverra vulputate eleifend.</p>
      <div class="scores"><b>Reliability</b>: 9.38 <b>Courtesy</b>:10 <b>Tidiness</b>:9.84</div>
      <div class="meta">Verified 28th September 2021 | Located in Brentwood</div>
      <div class="badge"><div class="brand">Fixrated.net</div><div class="badge-stars"><svg class="star"><use href="#star"/></svg><svg class="star"><use href="#star"/></svg><svg class="star"><use href="#star"/></svg><svg class="star"><use href="#star"/></svg><svg class="star"><use href="#star-pale"/></svg></div><div class="rating">4.2</div></div>
    </article>

    <div class="load">Load More</div>
  </section>

  <section class="panel panel-mobile">
    <div class="head-stars">
      <svg class="star"><use href="#star"/></svg><svg class="star"><use href="#star"/></svg><svg class="star"><use href="#star"/></svg><svg class="star"><use href="#star"/></svg><svg class="star"><use href="#star"/></svg>
    </div>
    <h1 class="title">Reviews</h1>
    <div class="subtitle">Combined Review Score 4.3 out of 5</div>
    <div class="filter-round"><svg width="16" height="14" viewBox="0 0 16 14" fill="none" stroke="#1d2330" stroke-width="1.2" stroke-linecap="round"><path d="M1 3h14M1 7h14M1 11h14"/><circle cx="10" cy="3" r="1.6" fill="#38bdf0"/><circle cx="5" cy="7" r="1.6" fill="#38bdf0"/><circle cx="11" cy="11" r="1.6" fill="#38bdf0"/></svg></div>

    <article class="review" style="top:113px">
      <h3>Front door with windows each side and side window</h3>
      <p>Lorem ipsum dolor sit amet, consectetur adipiscing elit. Tristique elementum maecenas purus dignissim felis.</p>
      <div class="scores"><b>Reliability</b>: 9.38 <b>Courtesy</b>:10 <b>Tidiness</b>:9.84</div>
      <div class="meta">Verified 28th September 2021 | Located in Brentwood</div>
      <div class="badge"><div class="brand">Fixrated.net</div><div class="badge-stars"><svg class="star"><use href="#star"/></svg><svg class="star"><use href="#star"/></svg><svg class="star"><use href="#star"/></svg><svg class="star"><use href="#star"/></svg><svg class="star"><use href="#star-pale"/></svg></div><div class="rating">4.2</div></div>
    </article>

    <article class="review active" style="top:200px">
      <h3>Front door with windows each side and side window</h3>
      <p>Lorem ipsum dolor sit amet, consectetur adipiscing elit. Tristique elementum maecenas purus dignissim felis.</p>
      <div class="scores"><b>Reliability</b>: 9.38 <b>Courtesy</b>:10 <b>Tidiness</b>:9.84</div>
      <div class="meta">Verified 28th September 2021 | Located in Brentwood</div>
      <div class="badge"><div class="brand">Fixrated.net</div><div class="badge-stars"><svg class="star"><use href="#star"/></svg><svg class="star"><use href="#star"/></svg><svg class="star"><use href="#star"/></svg><svg class="star"><use href="#star"/></svg><svg class="star"><use href="#star-pale"/></svg></div><div class="rating">4.2</div></div>
    </article>

    <article class="review" style="top:287px">
      <h3>Front door with windows each side and side window</h3>
      <p>Lorem ipsum dolor sit amet, consectetur adipiscing elit. Tristique elementum maecenas purus dignissim felis.</p>
      <div class="scores"><b>Reliability</b>: 9.38 <b>Courtesy</b>:10 <b>Tidiness</b>:9.84</div>
      <div class="meta">Verified 28th September 2021 | Located in Brentwood</div>
      <div class="badge"><div class="brand">Fixrated.net</div><div class="badge-stars"><svg class="star"><use href="#star"/></svg><svg class="star"><use href="#star"/></svg><svg class="star"><use href="#star"/></svg><svg class="star"><use href="#star"/></svg><svg class="star"><use href="#star-pale"/></svg></div><div class="rating">4.2</div></div>
    </article>

    <article class="review" style="top:374px">
      <h3>Front door with windows each side and side window</h3>
      <p>Lorem ipsum dolor sit amet, consectetur adipiscing elit. Tristique elementum maecenas purus dignissim felis.</p>
      <div class="scores"><b>Reliability</b>: 9.38 <b>Courtesy</b>:10 <b>Tidiness</b>:9.84</div>
      <div class="meta">Verified 28th September 2021 | Located in Brentwood</div>
      <div class="badge"><div class="brand">Fixrated.net</div><div class="badge-stars"><svg class="star"><use href="#star"/></svg><svg class="star"><use href="#star"/></svg><svg class="star"><use href="#star"/></svg><svg class="star"><use href="#star"/></svg><svg class="star"><use href="#star-pale"/></svg></div><div class="rating">4.2</div></div>
    </article>

    <div class="load">Load More</div>

    <nav class="nav">
      <div class="nav-item current"><svg viewBox="0 0 12 12"><path d="M1.5 10.5V5.5L6 1.5l4.5 4v5z" stroke-linejoin="round"/><path d="M4 8h4"/></svg>Home</div>
      <div class="nav-item"><svg viewBox="0 0 12 12"><circle cx="6" cy="4" r="1.8"/><path d="M2.5 10c0-2 1.5-3.2 3.5-3.2S9.5 8 9.5 10"/><circle cx="2" cy="5" r="1.2"/><circle cx="10" cy="5" r="1.2"/></svg>Contacts</div>
      <div class="nav-item"><svg viewBox="0 0 12 12"><circle cx="6" cy="6" r="4.8"/><path d="M1.2 6h9.6M6 1.2c1.6 1.5 1.6 8.1 0 9.6M6 1.2c-1.6 1.5-1.6 8.1 0 9.6"/></svg>Services</div>
      <div class="nav-item"><svg viewBox="0 0 12 12"><path d="M6 1.5a4.5 4.2 0 1 1-2.4 7.8L1.5 10.5l.8-2.2A4.5 4.2 0 0 1 6 1.5z" stroke-linejoin="round"/><path d="M4 6h.1M6 6h.1M8 6h.1"/></svg>Messages</div>
      <div class="nav-item"><svg viewBox="0 0 12 12"><circle cx="6" cy="6" r="1.7"/><path d="M6 1l1.2 1.3 1.7-.3.5 1.7 1.6.7-.5 1.6.5 1.6-1.6.7-.5 1.7-1.7-.3L6 11l-1.2-1.3-1.7.3-.5-1.7-1.6-.7.5-1.6-.5-1.6 1.6-.7.5-1.7 1.7.3z" stroke-linejoin="round"/></svg>Settings</div>
    </nav>
  </section>
</div>
</body>
</html>
```